Campus Rebate Desk business needs a advertisment design

We need a advertisment design for a handout which is going on the back of a local map.

The final advert will be 94 mm x 133mm

We are based in a town by the sea in Australia and our target market is young international students. So the advert needs to feel fun whilst being trustworthy.

Apparently we need the final artwork in a high res CMYK print ready PDF file with all fonts embedded & a 3mm bleed. The dimensions must be 94 mm x 133mm The advert is in portrate

Target Market(s)

Young International Students

Industry/Entity Type

Town

Requirements
Must have
• The advert needs to include our logo (Attached)
Wording in our font (also attached)
And our colour yellow, which is #ffdc00

```html
<!DOCTYPE html>
<html lang="en">
<head>
<meta charset="utf-8">
<title>Campus Rebate Desk – Get your tax refund</title>
<link rel="stylesheet" href="https://fonts.googleapis.com/css2?family=Lato:wght@700;900&display=swap">
<style>
  :root {
    --brand-yellow: #ffdc00;
    --ink: #000000;
    --paper: #ffffff;
    --photo-light: #e9e4da;
    --photo-mid: #c9bfae;
  }
  * { margin: 0; padding: 0; box-sizing: border-box; }
  html, body { width: 847px; height: 1200px; overflow: hidden; background: var(--paper); }
  .advert {
    position: relative;
    width: 847px;
    height: 1200px;
    font-family: "Lato", Arial, sans-serif;
    font-weight: 700;
    color: var(--ink);
    overflow: hidden;
  }
  .header {
    position: absolute; left: 0; top: 0; width: 100%; height: 343px;
    background: var(--brand-yellow);
  }
  .brand {
    position: absolute; top: 62px; left: 0; width: 100%;
    display: flex; justify-content: center; align-items: center; gap: 12px;
    font-size: 26px; font-weight: 900; letter-spacing: 0.2px;
  }
  .brand-mark { width: 22px; height: 22px; background: var(--ink); }
  .headline {
    position: absolute; top: 188px; left: 0; width: 100%;
    text-align: center; font-size: 52px; line-height: 62px; letter-spacing: 0.3px;
  }
  .band-top {
    position: absolute; left: 0; top: 343px; width: 100%; height: 41px;
    background: var(--ink);
  }
  .visual {
    position: absolute; left: 0; top: 384px; width: 100%; height: 449px;
    background: var(--paper);
  }
  .visual-photo {
    position: absolute; left: 0; top: 25px; width: 508px; height: 417px;
    background: linear-gradient(90deg, #2a3f8c 0%, #b8353a 22%, var(--photo-light) 40%, var(--photo-mid) 100%);
    border-radius: 0 40px 40px 0;
  }
  .question-mark {
    position: absolute; left: 520px; top: 30px; width: 230px;
    text-align: center; font-family: "Lato", Arial, sans-serif; font-weight: 700;
    font-size: 420px; line-height: 400px;
  }
  .rule {
    position: absolute; left: 0; top: 833px; width: 100%; height: 10px;
    background: var(--ink);
  }
  .cta {
    position: absolute; left: 0; top: 843px; width: 100%; height: 131px;
    background: var(--brand-yellow);
    display: flex; align-items: center; justify-content: center;
    font-size: 72px; font-weight: 900;
  }
  .contact {
    position: absolute; left: 0; top: 974px; width: 100%; height: 110px;
    background: var(--ink); color: var(--brand-yellow);
    display: flex; flex-direction: column; align-items: center; justify-content: center;
    font-size: 29px; line-height: 44px;
  }
  .footer {
    position: absolute; left: 0; top: 1084px; width: 100%; height: 116px;
    background: var(--brand-yellow);
    display: flex; align-items: center; justify-content: center;
    font-size: 29px;
  }
</style>
</head>
<body>
<main class="advert">
  <section class="header">
    <div class="brand"><span class="brand-mark"></span><span class="brand-name">Campus Rebate Desk</span></div>
    <h1 class="headline">At the end of June or<br>when you’re leaving Australia</h1>
  </section>
  <div class="band-top"></div>
  <section class="visual">
    <div class="visual-photo" role="img" aria-label="Photo of an arm in a striped costume sleeve and white glove holding out a cloth sack stamped Tax Refund"></div>
    <div class="question-mark" aria-hidden="true">?</div>
  </section>
  <div class="rule"></div>
  <h2 class="cta">Get your tax refund</h2>
  <section class="contact">
    <p class="contact-web">www.campusrebatedesk.com</p>
    <p class="contact-address">14 Harbour Rd. Seacliff 1300 482 907</p>
  </section>
  <footer class="footer">A product of Wanderers Mate</footer>
</main>
</body>
</html>
```